8 1/2 x 11 Flyer mailer for Window Envelope.

I need a flyer/mailer advertisement for a 9x12 window envelope. The front page needs to have text from a Word document which I will be uploading. A colorful header with our logo, phone number, fax number, mailing address, and website need to be at the top.

Just below the header needs to be an open white space where we can print addresses for the bulk mailing. The White space is from the Date on word docs uploaded all the way down to the Dear etc. It needs to be white and open f so that we can run the flyer through a printer to print the address, date, and dear mr: specifically and most importantly that the address may appear through the window.

General pictures of the lawyers and company colors on the front page with provided text.

On the back of the flyer we would like full color with a map to our office, preferably like the one we have on our website, along with practice areas and the info from our website. Including the about us portion, and the excerpts from the front of our website

www.DesertDefenseCounsel.example

The Back of the flyer can be the same for each of the 5 flyers, but the text on the front needs to reflect the text in the five word documents I have uploaded.
Updates

To be more specific for the Flyer.  The flyer should be like a letterhead on the front, with the text from the letter I am currently using.  With a footer as well with our website address and phone number at the bottom.

The back of the flyer should look like the half page flyer I posted with the design.

```html
<!DOCTYPE html>
<html lang="en">
<head>
<meta charset="utf-8">
<title>Desert Defense Counsel – DWI Letter Mailer</title>
<link href="https://fonts.googleapis.com/css2?family=Roboto:wght@300;400&family=Cormorant+Garamond:wght@500&display=swap" rel="stylesheet">
<style>
  :root {
    --ink-black: #0b0b0b;
    --paper: #ffffff;
    --body-grey: #6a6a6a;
    --dark-grey: #2a2a2a;
    --footer-text: #f2f2f2;
    --stone-light: #d9d9d9;
    --stone-dark: #6e6e6e;
    --wood-dark: #3a241a;
    --wood-mid: #7a4a32;
    --suit-grey: #8d8a88;
  }
  * { box-sizing: border-box; margin: 0; padding: 0; }
  html, body { width: 945px; height: 1200px; overflow: hidden; background: var(--paper); }
  .flyer { position: relative; width: 945px; height: 1200px; background: var(--paper); font-family: "Roboto", Arial, sans-serif; }

  .columns-photo { position: absolute; left: 0; top: 0; width: 699px; height: 164px;
    background: linear-gradient(90deg, var(--stone-dark) 0%, var(--stone-light) 12%, #9a9a9a 22%, var(--stone-light) 34%, #8a8a8a 48%, #ececec 64%, #a8a8a8 80%, #f0f0f0 100%); }
  .corner-block { position: absolute; left: 699px; top: 0; width: 246px; height: 164px; background: var(--ink-black); }
  .desk-photo { position: absolute; left: 699px; top: 164px; width: 246px; height: 943px;
    background: linear-gradient(180deg, #3b3b3b 0%, var(--suit-grey) 18%, #c9c3bf 30%, #5a4a44 48%, var(--wood-mid) 62%, var(--wood-dark) 80%, #5e3a28 100%); }

  .title-band { position: absolute; left: 0; top: 164px; width: 699px; height: 192px; background: var(--ink-black);
    display: flex; align-items: flex-end; padding: 0 0 30px 76px; }
  .title-band h1 { color: var(--paper); font-weight: 400; font-size: 30.5px; line-height: 41px; letter-spacing: 0.1px; }

  .letter { position: absolute; left: 0; top: 356px; width: 699px; height: 751px; background: var(--paper);
    padding: 36px 36px 0 102px; color: var(--body-grey); font-size: 12.4px; line-height: 17.4px; font-weight: 300; }
  .letter p { margin-bottom: 7px; text-align: justify; }
  .letter .date, .letter .addressee, .letter .signature { color: var(--dark-grey); font-weight: 400; }
  .letter .date { margin-bottom: 12px; }
  .letter .recipient { margin-bottom: 6px; text-align: left; }
  .letter .questions { list-style: none; margin: 4px 0 6px 120px; }
  .letter .questions li { margin-bottom: 8.5px; }
  .letter .questions li::before { content: "•"; margin-right: 7px; }
  .letter .signature { margin-top: 12px; text-align: left; }

  .footer { position: absolute; left: 0; top: 1107px; width: 945px; height: 93px; background: var(--ink-black);
    color: var(--footer-text); }
  .brand { position: absolute; left: 28px; top: 24px; display: flex; align-items: center; gap: 18px; }
  .brand-circle { width: 42px; height: 42px; border: 1.5px solid var(--footer-text); border-radius: 50%; }
  .brand-name { font-family: "Cormorant Garamond", Georgia, serif; font-weight: 500; font-size: 21px; line-height: 22px;
    letter-spacing: 1.6px; text-transform: uppercase; }
  .contact, .address { position: absolute; top: 18px; font-size: 13px; line-height: 18.5px; white-space: nowrap; }
  .contact { left: 400px; }
  .address { left: 668px; }
</style>
</head>
<body>
<div class="flyer">
  <div class="columns-photo" role="img" aria-label="Black and white photograph of classical courthouse columns"></div>
  <div class="corner-block"></div>
  <div class="desk-photo" role="img" aria-label="Photograph of a lawyer in suit and tie at a wooden desk with a judge's gavel"></div>

  <header class="title-band">
    <h1>New Mexico DWI laws provide for<br>serious and mandatory criminal penalties</h1>
  </header>

  <main class="letter">
    <p class="date">December 23, 2013</p>
    <p class="recipient">To,<br><span class="addressee">Abc</span></p>
    <p>Dear «4»:</p>
    <p>Public records show that you were recently and unfortunately charged with DWI. It is veryimportant that you know your rights and obligations in this matter and that you receive the best possible legal representation. New Mexico DWI laws provide for serious and mandatory criminal penalties. Some important questions you need answered are:</p>
    <ul class="questions">
      <li>What are the maximum possible fines and penalties?</li>
      <li>Do I face mandatory jail time?</li>
      <li>Will my driver’s license be revoked?</li>
    </ul>
    <p>IMPORTANT: You have only 10 days from the date of your arrest to request an MVD Hearing and pay the $25 administrative hearing fee.We have enclosed an MVD Hearing request for this purpose. If you contact our office within 5 days from the date of your arrest we will guarantee to represent you at your MVD hearing for no additional charge.If you miss this deadline your driving privilege will be automatically revoked for six months or longer. The MVD License Revocation Hearing is a separate hearing from your criminal case in Metropolitan Court. Call us for assistance in submitting this MVD Hearing request.</p>
    <p>Call 555-0142 for a free evaluation of your case. You will need all paperwork regarding your case for a proper evaluation. In reviewing the individual facts of your case, we will determine whether the officers who made contact with you followed the proper procedure. We will also help you examine all of your options and determine whether the judge assigned to your case should be excused.</p>
    <p>We are members of the Southwest Defense Bar Association, and have combined 22 years of experience in defending DUI cases. Our fees are designed to beaffordable to you.We will meet with you at your convenience.</p>
    <p>CALL 555-0142 FOR A FREE CASE EVALUATION AND CONSULTATION. You may decide you do not need an attorney but make an informed decision.</p>
    <p>Weare members of the Southwest Defense Bar Association, and we have more than 23 years combined experience in defending Domestic Violence cases. Our fees are designed to be affordable to you. We will meet with you at your convenience.</p>
    <p>Sincerely,</p>
    <p class="signature">Desert Defense Counsel<br>Attorneys at Law</p>
  </main>

  <footer class="footer">
    <div class="brand">
      <div class="brand-circle"></div>
      <div class="brand-name">Desert Defense<br>Counsel</div>
    </div>
    <div class="contact">
      P : (505) 555-0142<br>
      F : (505) 555-0187<br>
      W : www.DesertDefenseCounsel.example
    </div>
    <div class="address">
      2140 Mesa Verde Ave.<br>
      NW Albuquerque<br>
      NM 87104
    </div>
  </footer>
</div>
</body>
</html>
```